Steady Harbor Leadership Roundtable Series Promotion

I'm wanting a single page (for now) website to promote my leadership training. Content would include: basic messaging what Steady Harbor means, invitation to join the Steady Harbor Roundtable workshops, have me come speak to them, join me on a leadership getaway, get personal coaching, watch some video links of Rud, then referrals of people saying nice things about Rud, connect to Rud’s personal website to learn more about me. The goal of the page is to 1) get people excited to attend a workshop, hear me speak, coach them, or join me on a getaway trip, 2) educate them in how they can get in control of their own life, and 3) link to my personal site to learn more about me. This is the general idea: https://www.perlwickstand.com/

Target Market(s)

Business owners or self improvement enthusiasts looking to take their businesses and personal lives to the next level.

Industry/Entity Type

Business Consultant

Coding

Coded - Design and coding required

Number of Pages Required

1 page

Font styles to use
Other font styles liked:
• See uploaded logo

Colors
0392cd

Requirements
Must have
• Fonts and colors that match the logo that was uploaded. Uplifting, inspirational look and feel.
Nice to have
• Similar to: https://www.perlwickstand.com/ and https://dorvankessling.com/

```html
<!DOCTYPE html>
<html lang="en">
<head>
<meta charset="utf-8">
<title>Steady Harbor — Transform Your Life</title>
<link rel="stylesheet" href="https://fonts.googleapis.com/css2?family=Noto+Serif:ital,wght@0,400;0,700;1,400&family=Noto+Sans:ital,wght@0,400;0,600;0,700;1,400&display=swap">
<style>
:root{
  --brand:#1fb0e6;
  --brand-deep:#0392cd;
  --ink:#111;
  --text:#555;
  --muted:#777;
  --dark:#1b1b1d;
  --white:#fff;
  --line:#e3e3e3;
  --serif:"Noto Serif", Georgia, serif;
  --sans:"Noto Sans", Arial, sans-serif;
}
*{box-sizing:border-box;margin:0;padding:0}
html,body{width:1200px;height:4277px;overflow:hidden;background:var(--white)}
body{font-family:var(--sans);color:var(--text)}
.page{position:relative;width:1200px;height:4277px;overflow:hidden}
.abs{position:absolute}
a{color:inherit;text-decoration:none}
.img{position:absolute;display:block}

/* top bar */
.topbar{left:0;top:0;width:1200px;height:53px;background:#000;color:#fff;font-size:12px}
.topbar .ic{position:absolute;top:9px;width:35px;height:35px;border-radius:50%;background:var(--brand);display:flex;align-items:center;justify-content:center}
.topbar span{position:absolute;top:18px}

/* nav */
.nav{left:0;top:53px;width:1200px;height:90px;background:#fff}
.wordmark{font-family:var(--serif);font-weight:700;color:var(--brand-deep);letter-spacing:2px;display:flex;align-items:center;gap:8px}
.wordmark i{display:block;width:12px;height:12px;background:var(--brand-deep)}
.menu{position:absolute;top:36px;left:449px;display:flex;gap:0;font-family:var(--serif);font-weight:700;font-size:12px;color:#222}
.menu a{margin-right:40px}
.menu a.on{color:var(--brand);font-weight:400}

/* hero */
.hero{left:0;top:143px;width:1200px;height:640px;background:linear-gradient(100deg,#4a4d50 0%,#2c2f33 35%,#3d4246 60%,#55595c 100%)}
.hero h1{position:absolute;top:150px;width:1200px;text-align:center;font-family:var(--serif);font-weight:700;font-size:58px;color:#fff;letter-spacing:1px}
.hero p{position:absolute;top:235px;width:1200px;text-align:center;font-weight:700;font-size:16px;color:var(--brand);letter-spacing:.3px}
.btn{position:absolute;display:flex;align-items:center;justify-content:center;border-radius:30px;font-family:var(--serif);font-size:16px}
.btn.fill{background:var(--brand);color:#fff}
.btn.line{border:2px solid var(--brand);color:var(--brand);background:transparent}

/* headings */
.h2{font-family:var(--serif);font-weight:700;color:var(--ink);font-size:30px;line-height:1.2;letter-spacing:.3px}
.sub{font-weight:600;font-size:12px;color:var(--brand)}
.body{font-size:12.5px;line-height:20px;color:var(--text)}

/* about */
.about-card{left:161px;top:823px;width:589px;height:226px;background:#fff;box-shadow:0 0 10px rgba(0,0,0,.15);padding:30px 33px}
.about-card p{margin-top:14px;font-style:italic;font-size:13.5px;line-height:22px;color:#555}

/* tiles */
.tile-label{position:absolute;left:0;bottom:0;width:100%;height:46px;background:rgba(40,40,40,.7);color:#fff;font-family:var(--serif);font-weight:700;font-size:14px;display:flex;align-items:center;justify-content:center}
.media-label{position:absolute;left:0;bottom:0;width:100%;height:53px;background:rgba(31,176,230,.85);color:#fff;font-family:var(--serif);font-weight:700;font-size:15px;display:flex;align-items:center;justify-content:center}

/* join */
.join-card{left:161px;top:1979px;width:878px;height:227px;background:#fff;box-shadow:0 0 10px rgba(0,0,0,.15);text-align:center}

/* testimonial */
.quote-card{left:279px;top:2860px;width:639px;height:249px;background:#fff;box-shadow:0 0 10px rgba(0,0,0,.15);text-align:center}
.dots{display:flex;gap:7px;justify-content:center}
.dots i{width:8px;height:8px;border-radius:50%;border:1px solid var(--brand)}
.dots i.on{background:var(--brand)}

/* events */
.event{position:absolute;left:161px;width:430px;height:90px}
.event .thumb{position:absolute;left:0;top:0;width:143px;height:90px}
.event .date{position:absolute;left:0;top:0;width:36px;height:36px;background:var(--brand);color:#fff;text-align:center;font-family:var(--serif);font-size:16px;line-height:18px;padding-top:2px}
.event .date small{display:block;font-family:var(--sans);font-size:8px;line-height:10px}
.event .txt{position:absolute;left:158px;top:0;width:272px}
.event h4{font-family:var(--serif);font-size:12.5px;color:#111}
.event .when{font-size:9px;color:var(--brand);margin-top:3px}
.event p{font-size:10.5px;line-height:17px;color:#666;margin-top:2px}
.event .more{font-size:10px;font-weight:700;color:var(--brand)}

/* cta */
.cta-card{left:161px;top:3727px;width:878px;height:113px;background:#fff;box-shadow:0 0 10px rgba(0,0,0,.2)}

/* footer */
.footer{left:0;top:3781px;width:1200px;height:449px;background:linear-gradient(180deg,#1c1d20,#121314)}
.footer h5{position:absolute;top:146px;font-family:var(--serif);font-weight:400;font-size:15px;color:#fff;letter-spacing:.5px}
.footer ul{position:absolute;top:190px;list-style:none;font-size:11.5px;color:#ddd}
.footer li{height:24px;display:flex;align-items:center;gap:9px}
.footer li::before{content:"";width:6px;height:6px;border-radius:50%;border:1px solid var(--brand)}
.contact{position:absolute;left:838px;font-size:11.5px;color:#eee;display:flex;gap:14px;align-items:center;line-height:15px}
.social{position:absolute;top:4148px;left:465px;display:flex;gap:9px}
.social i{display:block;width:36px;height:36px;border-radius:50%;border:1px solid #fff}
.social i.on{background:var(--brand);border-color:var(--brand)}
.copy{left:0;top:4230px;width:1200px;height:47px;background:var(--brand);color:#fff;font-size:12px;display:flex;align-items:center;justify-content:center}
</style>
</head>
<body>
<div class="page">

  <!-- top bar -->
  <div class="abs topbar">
    <div class="ic" style="left:161px"><svg width="16" height="12" viewBox="0 0 16 12"><rect x="1" y="1" width="14" height="10" fill="none" stroke="#fff" stroke-width="1.5"/><path d="M1 1l7 6 7-6" fill="none" stroke="#fff" stroke-width="1.5"/></svg></div>
    <span style="left:212px">support@steadyharbor.com</span>
    <div class="ic" style="left:898px"><svg width="16" height="16" viewBox="0 0 16 16"><path d="M3 1l3 3-2 2c1 2 3 4 5 5l2-2 3 3-2 3C6 15 1 10 1 3z" fill="#fff"/></svg></div>
    <span style="left:952px">1-855-555-0147</span>
  </div>

  <!-- nav -->
  <header class="abs nav">
    <div class="abs wordmark" style="left:161px;top:30px;font-size:22px"><i></i>STEADY HARBOR</div>
    <nav class="menu">
      <a href="#">Workshop</a><a href="#" class="on">Video</a><a href="#">About Me</a><a href="#">Coaching</a><a href="#">Join Me</a><a href="#">Resources</a>
    </nav>
    <svg class="abs" style="left:995px;top:36px" width="20" height="20" viewBox="0 0 20 20"><circle cx="8" cy="8" r="6" fill="none" stroke="#bbb" stroke-width="2.5"/><path d="M12.5 12.5l6 6" stroke="#bbb" stroke-width="3"/></svg>
  </header>

  <!-- hero -->
  <section class="abs hero">
    <div class="img" role="img" aria-label="Photo of a film crew with a camera on a waterfront at dusk" style="inset:0;background:linear-gradient(90deg,rgba(0,0,0,.15),rgba(0,0,0,.35),rgba(0,0,0,.1))"></div>
    <h1>TRANSFORM YOUR LIFE</h1>
    <p>DECADES OF EXPERIENCE. MILLIONS OF LIVES CHANGED. UNDENIABLE RESULTS.</p>
    <a class="btn fill" href="#" style="left:435px;top:300px;width:149px;height:48px">Login Now</a>
    <a class="btn line" href="#" style="left:614px;top:300px;width:151px;height:48px">Call Us Now!</a>
  </section>
  <svg class="abs" style="left:0;top:640px" width="1200" height="150" viewBox="0 0 1200 150">
    <path d="M0 80 C220 160 420 140 620 90 C800 40 960 10 1200 60 L1200 150 L0 150Z" fill="#fff"/>
    <path d="M0 75 C220 150 420 130 620 82 C800 32 960 0 1200 55 L1200 80 C960 20 800 55 620 100 C420 150 220 170 0 100Z" fill="var(--brand)"/>
    <path d="M0 96 C220 170 420 150 620 100 C800 50 960 18 1200 72 L1200 82 C960 28 800 60 620 108 C420 160 220 178 0 108Z" fill="#fff"/>
  </svg>

  <!-- about -->
  <div class="img" role="img" aria-label="Portrait of the coach seated in an office" style="left:611px;top:805px;width:589px;height:262px;background:linear-gradient(90deg,#d7e2e6,#b7c6cc 50%,#8d9aa0)"></div>
  <section class="abs about-card">
    <h2 class="h2">ABOUT ME</h2>
    <p>Live a healthier, wealthier, more fulfilling, passionate and purposeful life – whether that means achieving in business, reigniting your relationship or discovering who you really are. Rud Halvorsen's live events, one-on-one coaching program, training systems and group workshops will help close the gap between where you are and where you want to be.</p>
  </section>

  <!-- master -->
  <h2 class="abs h2" style="left:163px;top:1118px;width:420px">MASTER EVERY AREA OF YOUR LIFE</h2>
  <div class="abs sub" style="left:163px;top:1192px">Solutions To Fit Your Time, Your Lifestyle And Your Budget</div>
  <p class="abs body" style="left:612px;top:1141px;width:425px">Lorem Ipsum is simply dummy text of the printing and typesetting industry. Lorem Ipsum has been the industry's standard dummy text ever since the 1500s,</p>

  <div class="img" role="img" aria-label="Photo of guests at a live event" style="left:161px;top:1268px;width:203px;height:202px;background:linear-gradient(160deg,#5d6a61,#2f3a36)"><span class="tile-label">LIFE EVENTS</span></div>
  <div class="img" role="img" aria-label="Photo of a speaker on stage" style="left:387px;top:1268px;width:202px;height:202px;background:linear-gradient(160deg,#e6e4df,#b9b5ae)"><span class="tile-label">PRIVATE COACHING</span></div>
  <div class="img" role="img" aria-label="Photo of a stone bridge over a forest lake" style="left:611px;top:1268px;width:203px;height:202px;background:linear-gradient(180deg,#6f9fc4,#3f6b3a 50%,#26401f)"><span class="tile-label">EXCLUSIVE RATREATS</span></div>
  <div class="img" role="img" aria-label="Photo of a team meeting in a bright office" style="left:837px;top:1268px;width:202px;height:202px;background:linear-gradient(160deg,#eef0f1,#c4c8cb)"><span class="tile-label">TRAINING PROGRAMS</span></div>

  <a class="btn fill" href="#" style="left:544px;top:1535px;width:112px;height:37px;font-size:15px">View All</a>

  <!-- video -->
  <div class="img" role="img" aria-label="Video still of the coach speaking to an audience" style="left:161px;top:1638px;width:428px;height:264px;border-radius:8px;background:radial-gradient(circle at 40% 40%,#4a4f7a,#1e2040 70%)">
    <svg class="abs" style="left:174px;top:92px" width="80" height="80" viewBox="0 0 80 80"><circle cx="40" cy="40" r="38" fill="rgba(31,176,230,.35)"/><circle cx="40" cy="40" r="26" fill="var(--brand)"/><path d="M34 28l16 12-16 12z" fill="#fff"/></svg>
  </div>
  <h2 class="abs h2" style="left:612px;top:1640px">DRIVEN BY PURPOSE</h2>
  <div class="abs sub" style="left:612px;top:1676px;font-size:11px">40 Years Of Helping Others Create Success And Fulfillment</div>
  <p class="abs body" style="left:612px;top:1715px;width:430px">Rud Halvorsen is an entrepreneur, best-selling author, philanthropist and the nation's #1 Life and Business Strategist. He has dedicated his life to helping people discover their true purpose and leverage their unique gifts to achieve massive success – to make their life a true masterpiece. If you're feeling stuck, or unsure of your next step, Rud will lead you to clarity, focus and action.</p>
  <a class="btn fill" href="#" style="left:611px;top:1861px;width:135px;height:35px;font-size:14px">Rud's Full Bio</a>

  <!-- join + media band -->
  <div class="img" role="img" aria-label="Photo of a conference hall audience" style="left:0;top:2070px;width:1200px;height:427px;background:linear-gradient(90deg,#2a2430,#3a3450 50%,#2a2d3c)"></div>
  <section class="abs join-card">
    <h2 class="h2" style="font-size:26px;margin-top:40px">JOIN NOW TO STEADY HARBOR ROUNDTABLE</h2>
    <p class="body" style="width:600px;margin:14px auto 0">Lorem Ipsum is simply dummy text of the printing and typesetting industry. Lorem Ipsum has been the industry's standard dummy text ever since the 1500s,</p>
    <a class="btn line" href="#" style="left:383px;top:148px;width:112px;height:36px;font-size:15px">Join Now</a>
  </section>
  <h2 class="abs h2" style="left:0;top:2256px;width:1200px;text-align:center;color:#fff;letter-spacing:2px">READ. WATCH. LISTEN.</h2>
  <div class="abs sub" style="left:0;top:2292px;width:1200px;text-align:center;font-size:11px">Get Started Now With Insights And Strategies From Rud Halvorsen</div>

  <div class="img" role="img" aria-label="Photo of two business people walking" style="left:161px;top:2364px;width:277px;height:277px;background:linear-gradient(160deg,#8a7565,#4b3d33)"><span class="media-label">Blog</span></div>
  <div class="img" role="img" aria-label="Photo of a man wearing studio headphones" style="left:461px;top:2364px;width:278px;height:277px;background:linear-gradient(160deg,#d8733a,#4a2c20)">
    <div class="abs" style="left:0;top:126px;width:278px;height:151px;background:rgba(31,176,230,.88);color:#fff;text-align:center">
      <div style="font-family:var(--serif);font-weight:700;font-size:15px;margin-top:22px">Podcast</div>
      <p style="font-size:11.5px;line-height:19px;width:240px;margin:10px auto 0">Lorem Ipsum is simply dummy text of the printing and typesetting industry. Lorem Ipsum has been the industry's standard dummy text ever since the 1500s,</p>
    </div>
  </div>
  <div class="img" role="img" aria-label="Photo of a cameraman filming" style="left:760px;top:2364px;width:279px;height:277px;background:linear-gradient(160deg,#c5d3dd,#5e6870)"><span class="media-label">Video</span></div>

  <!-- success stories -->
  <h2 class="abs h2" style="left:0;top:2699px;width:1200px;text-align:center">SUCCESS STORIES</h2>
  <div class="abs sub" style="left:0;top:2739px;width:1200px;text-align:center;font-size:11px">What People Say About Our Company</div>
  <section class="abs quote-card">
    <div style="color:var(--brand);font-size:13px;margin-top:76px">-Owen Castell</div>
    <p style="font-style:italic;font-size:14px;line-height:30px;color:#666;width:590px;margin:6px auto 0">Lorem Ipsum is simply dummy text of the printing and typesetting industry. Lorem Ipsum has been the industry's standard dummy text ever since the 1500s, Lorem Ipsum is simply dummy text of the printing and typesetting industry. Lorem Ipsum has been the industry's standard dummy text ever since the 1500s,</p>
    <div class="dots" style="margin-top:14px"><i></i><i class="on"></i><i></i><i></i></div>
  </section>
  <div class="img" role="img" aria-label="Portrait of the client giving the testimonial" style="left:536px;top:2791px;width:126px;height:126px;border-radius:50%;border:3px solid var(--brand);background:linear-gradient(180deg,#e9eef1,#9fb0ba)"></div>

  <!-- events -->
  <h2 class="abs h2" style="left:163px;top:3176px">UPCOMAING EVENTS</h2>
  <div class="abs sub" style="left:163px;top:3217px;font-size:11px">Full Immersion. Life-Changing Experiences. Astounding Results.</div>

  <div class="event" style="top:3287px">
    <div class="thumb img" role="img" aria-label="Event photo of a speaker on stage" style="background:linear-gradient(160deg,#2c3d6a,#0f1630)"></div>
    <div class="date">7<small>July</small></div>
    <div class="txt"><h4>Lorem Ipsum is simply dummy text of the.</h4><div class="when">07 July 2019</div><p>Lorem Ipsum is simply dummy text of the printing and typesetting industry. Lorem....</p><div class="more">READ MORE</div></div>
  </div>
  <div class="event" style="top:3396px">
    <div class="thumb img" role="img" aria-label="Event photo of a speaker with raised arms" style="background:linear-gradient(160deg,#3d5a8c,#101a33)"></div>
    <div class="date">15<small>July</small></div>
    <div class="txt"><h4>Lorem Ipsum is simply dummy text of the.</h4><div class="when">15 July 2019</div><p>Lorem Ipsum is simply dummy text of the printing and typesetting industry. Lorem....</p><div class="more">READ MORE</div></div>
  </div>
  <div class="event" style="top:3506px">
    <div class="thumb img" role="img" aria-label="Event photo of a speaker in a suit" style="background:linear-gradient(160deg,#8f9296,#3d3f43)"></div>
    <div class="date">25<small>June</small></div>
    <div class="txt"><h4>Lorem Ipsum is simply dummy text of the.</h4><div class="when">25 June 2019</div><p>Lorem Ipsum is simply dummy text of the printing and typesetting industry. Lorem....</p><div class="more">READ MORE</div></div>
  </div>

  <h2 class="abs h2" style="left:612px;top:3176px">RUD'S EXTENDED FAMILY</h2>
  <div class="abs sub" style="left:614px;top:3217px;font-size:11px">Learn More About Rud's Work And Impact Around The World</div>
  <div class="img" role="img" aria-label="Photo of the coach laughing with friends" style="left:611px;top:3285px;width:428px;height:138px;background:linear-gradient(90deg,#5a2a1e,#9a5a3a 50%,#4a2418)"></div>
  <div class="img" role="img" aria-label="Photo of the coach with a colleague on a private jet" style="left:611px;top:3448px;width:428px;height:138px;background:linear-gradient(90deg,#8a6a4a,#d2b690 50%,#7a5a3a)"></div>

  <a class="btn fill" href="#" style="left:287px;top:3640px;width:173px;height:35px;font-size:15px">See Events Details</a>
  <a class="btn fill" href="#" style="left:769px;top:3640px;width:111px;height:35px;font-size:15px">View All</a>

  <!-- footer -->
  <footer class="abs footer">
    <div class="img" role="img" aria-label="Faint photo of the coach speaking" style="left:0;top:0;width:600px;height:449px;background:linear-gradient(90deg,rgba(60,60,66,.5),rgba(0,0,0,0))"></div>
    <div class="abs wordmark" style="left:161px;top:172px;font-size:22px;color:#fff"><i style="background:#fff"></i>STEADY HARBOR</div>
    <p class="abs" style="left:162px;top:234px;width:150px;font-size:11px;line-height:19px;color:#ddd">Lorem Ipsum is simply dummy text of the printing and typesetting industry. Lorem Ipsum has been the industry's standard dummy text ever since .</p>

    <h5 style="left:387px">QUICK LINKS</h5>
    <ul style="left:387px"><li>Workshop</li><li>Video</li><li>About Me</li><li>Coaching</li><li>Join Me</li><li>Resources</li></ul>

    <h5 style="left:613px">SERVICES</h5>
    <ul style="left:613px"><li>Sitemap</li><li>Careers</li><li>Terms</li><li>Policies</li><li>Return Policy</li><li>Affiliates</li></ul>

    <h5 style="left:838px">CONTACT INFO</h5>
    <div class="contact" style="top:220px"><svg width="20" height="20" viewBox="0 0 16 16"><path d="M3 1l3 3-2 2c1 2 3 4 5 5l2-2 3 3-2 3C6 15 1 10 1 3z" fill="var(--brand)"/></svg><span style="font-size:12.5px">1-855-555-0182</span></div>
    <div class="contact" style="top:260px"><svg width="20" height="24" viewBox="0 0 16 20"><path d="M8 0a7 7 0 0 1 7 7c0 5-7 13-7 13S1 12 1 7a7 7 0 0 1 7-7z" fill="var(--brand)"/><circle cx="8" cy="7" r="2.5" fill="#1c1d20"/></svg><span>4120 Lantern Cove Rd P.O. Box<br>30418, Marlow Bay, CA 90000</span></div>
    <div class="contact" style="top:312px"><svg width="20" height="15" viewBox="0 0 16 12"><rect x="0" y="0" width="16" height="12" fill="var(--brand)"/><path d="M0 0l8 7 8-7" fill="none" stroke="#1c1d20" stroke-width="1.5"/></svg><span>support@steadyharbor.<br>com</span></div>
  </footer>

  <div class="social"><i></i><i></i><i class="on"></i><i></i><i></i><i></i></div>

  <section class="abs cta-card">
    <h3 class="abs" style="left:54px;top:30px;font-family:var(--serif);font-size:22px;font-weight:400;color:var(--brand);letter-spacing:2px">START LIVING THE LIFE OF YOUR DREAMS</h3>
    <p class="abs" style="left:54px;top:67px;font-size:11.5px;color:#333">Don't know how to start? Our solution finder can help</p>
    <a class="btn line" href="#" style="left:673px;top:40px;width:121px;height:35px;font-size:11px;font-weight:700;letter-spacing:.5px">START TODAY</a>
  </section>

  <div class="abs copy">Copyright © 2019&nbsp;<b>Steady Harbor</b>. All rights reserved. Terms &amp; Conditions.</div>
</div>
</body>
</html>
```